Simple Easy - Taekwondo brochure

I have the content and an idea of the layout I want. I need it to look nice and sharp.

It's a sided 8.5x11 colored brochure

please feel free to move things around and use the images provided

my website is www.brightpathdojo.example if you need an understanding of what the business is about.

all text content is on the website. please be creative!

Target Market(s)

Mothers...must by family friendly because it's for mothers to bring their kids.

Industry/Entity Type

Martial Art

Font styles to use
Other font styles liked:
• Lato

```html
<!DOCTYPE html>
<html lang="en">
<head>
<meta charset="utf-8">
<title>Bright Path Dojo – Brochure Outside</title>
<link rel="stylesheet" href="https://fonts.googleapis.com/css2?family=Roboto+Condensed:wght@300;400;700&display=swap">
<style>
:root{
  --ink:#0b0b0c;
  --panel:#121213;
  --white:#ffffff;
  --text:#e9e9e9;
  --grey:#9a9a9a;
  --red:#d3202f;
  --blue:#1f6fc4;
  --page:#ececec;
}
*{box-sizing:border-box;margin:0;padding:0}
html,body{width:1200px;height:833px;overflow:hidden;background:var(--page)}
body{font-family:"Roboto Condensed",Arial,sans-serif;color:var(--text)}
.brochure{position:relative;width:1200px;height:833px;display:flex;background:var(--ink)}
.panel{position:relative;width:400px;height:833px;overflow:hidden}
.panel + .panel{border-left:1px solid #2a2a2a}

/* Bio panel */
.bio{background:var(--panel);padding:18px 20px 0 22px}
.bio p{font-size:10.6px;line-height:1.26;margin-bottom:11px;color:var(--text)}
.awards{position:relative;z-index:2;width:150px;margin-top:14px}
.awards h3{font-size:10.6px;font-weight:400;color:var(--red);line-height:1.2}
.awards .sub{font-size:10.6px;margin-bottom:10px;color:var(--text)}
.awards ul{list-style:none}
.awards li{position:relative;padding-left:14px;font-size:10.6px;line-height:1.22;margin-bottom:13px}
.awards li::before{content:"★";position:absolute;left:0;top:0;color:var(--blue);font-size:10px}
.instructor-photo{position:absolute;right:0;bottom:0;width:235px;height:300px;
  background:radial-gradient(ellipse at 50% 30%,#4a4a4c 0%,#2a2a2c 45%,#121213 80%)}

/* Contact panel */
.contact{background:var(--ink)}
.gi-photo{position:absolute;left:400px;top:0;width:800px;height:455px;
  background:linear-gradient(180deg,rgba(11,11,12,0) 55%,var(--ink) 100%),
             linear-gradient(90deg,#1b1b1c 0%,#8d8d8f 35%,#e6e6e6 55%,#cfcfcf 75%,#3a3a3c 100%)}
.map{position:absolute;left:78px;top:335px;width:246px;height:246px;border-radius:50%;
  border:5px solid var(--red);background:radial-gradient(circle at 45% 45%,#f1efe9 0%,#e2e0da 70%,#cfd6c8 100%)}
.contact-list{position:absolute;left:84px;top:592px;list-style:none}
.contact-list li{display:flex;align-items:flex-start;gap:14px;color:var(--white)}
.contact-list .addr{font-size:17px;line-height:1.22;margin-bottom:28px}
.contact-list .phone{font-size:17px;margin-bottom:30px;align-items:center}
.contact-list .social{font-size:13.5px;margin-bottom:14px;align-items:center}
.icon{flex:none;width:26px;height:26px}
.dot{flex:none;width:19px;height:19px;border-radius:50%;background:var(--blue);margin:0 4px 0 3px}
.dot.alt{background:var(--red)}

/* Cover panel */
.cover{background:transparent}
.cover-base{position:absolute;inset:455px 0 0 0;background:var(--ink)}
.stripe{position:absolute;left:0;top:370px;width:400px;height:90px}
.brand-mark{position:absolute;left:18px;top:395px;display:flex;align-items:center;gap:12px}
.brand-mark .circle{width:72px;height:72px;border-radius:50%;background:var(--blue)}
.brand-mark span{font-size:20px;font-weight:700;color:var(--white);letter-spacing:.5px}
.title{position:absolute;left:18px;top:586px;font-size:56px;line-height:.98;font-weight:700;color:var(--white);letter-spacing:.5px}
.tagline{position:absolute;left:18px;top:738px;font-size:21px;font-weight:300;color:var(--grey)}
.url{position:absolute;left:18px;top:786px;font-size:17px;font-weight:700;color:var(--white)}
.url em{font-style:normal;color:var(--red)}
</style>
</head>
<body>
<main class="brochure">
  <div class="gi-photo" role="img" aria-label="Photo of a student in a white uniform tying a black belt"></div>

  <section class="panel bio">
    <p>Daniel Cho (Master Dan) is the owner and head instructor at Bright Path Dojo. Master Dan is a Central Dan Council certified 3rd degree Black Belt. The Central Dan Council is the overseeing authority of all Black Belts in the world, working with the World Sport Taekwondo Union (WSTU); it also oversees taekwondo in the Olympics.</p>
    <p>In 1992, at the age of 8, Master Dan began training under Grand Master Ferraro who achieved the level of 8th Dan in taekwondo under the Global Taekwondo Alliance (GTA). The GTA is another highly respected global authority for taekwondo.</p>
    <p>When Master Dan entered Middle School and then High School, his years of taekwondo training became invaluable as he participated in wrestling, track, and hockey.</p>
    <p>Master Dan continued his taekwondo training post-high school, and in 2007, began training under Grand Master Baek who has achieved the level of 6th Dan in Taekwondo, certified by the Council. Grand Master Baek was also a distinguished member of the South Korean National Taekwondo Team that competed around the world.</p>
    <p>While attending Riverside University, Master Dan joined Riverside's Taekwondo Team. Upon graduating in 2008, he was invited by the University to become the team's Assistant Coach. Because of his exceptional skill and his ability to positively influence and motivate the team, the University selected him to lead as the coach of the team. Master Dan served as the Head Coach of Riverside University's Taekwondo Team from 2010-2013.</p>
    <p>In 2013, Master Dan began training under Grand Master Lim, a 9th Dan in Taekwondo, certified by the Council. Master Dan currently trains under Grand Master Lim.</p>
    <div class="awards">
      <h3>AWARDS / ACHIEVEMENTS</h3>
      <p class="sub">(under Master Dan's leadership)</p>
      <ul>
        <li>4 National Taekwondo League Championships / WSTU sanctioned</li>
        <li>10 State Medalists National Taekwondo League State Championships / WSTU sanctioned</li>
        <li>12 Atlantic Collegiate Taekwondo Circuit (ACTC) Team Medals / WSTU sanctioned</li>
        <li>1 Atlantic Collegiate Taekwondo Circuit (ACTC) TOP DIVISION TEAM TITLES / WSTU sanctioned</li>
      </ul>
    </div>
    <div class="instructor-photo" role="img" aria-label="Portrait of the head instructor in a white uniform with black collar"></div>
  </section>

  <section class="panel contact">
    <div class="map" role="img" aria-label="Street map showing the school location"></div>
    <ul class="contact-list">
      <li class="addr">
        <svg class="icon" viewBox="0 0 26 26"><circle cx="13" cy="13" r="12" fill="none" stroke="#1f6fc4" stroke-width="1.6"/><path d="M13 5.5a5 5 0 0 0-5 5c0 3.8 5 9.5 5 9.5s5-5.7 5-9.5a5 5 0 0 0-5-5z" fill="none" stroke="#1f6fc4" stroke-width="1.6"/><circle cx="13" cy="10.5" r="1.8" fill="#1f6fc4"/></svg>
        <span>2250 Orchard Lane<br>Maple Springs,<br>Pennsylvania</span>
      </li>
      <li class="phone">
        <svg class="icon" viewBox="0 0 26 26"><circle cx="13" cy="13" r="12" fill="none" stroke="#1f6fc4" stroke-width="1.6"/><path d="M9 6.5l2.3 3.2-1.4 1.6c.9 2 2.4 3.6 4.5 4.6l1.6-1.4 3.2 2.3-1.2 2.6c-5.6-.4-10-4.8-10.4-10.4z" fill="none" stroke="#1f6fc4" stroke-width="1.5" stroke-linejoin="round"/></svg>
        <span>+1 555-014-2290</span>
      </li>
      <li class="social"><span class="dot"></span><span>@brightpathdojo</span></li>
      <li class="social"><span class="dot alt"></span><span>brightpath__dojo</span></li>
    </ul>
  </section>

  <section class="panel cover">
    <div class="cover-base"></div>
    <svg class="stripe" viewBox="0 0 400 90" aria-hidden="true">
      <polygon points="230,40 400,12 400,30 240,56" fill="#d3202f"/>
      <polygon points="240,60 400,34 400,50 250,74" fill="#1f6fc4"/>
    </svg>
    <div class="brand-mark"><div class="circle"></div><span>BRIGHT PATH DOJO</span></div>
    <h1 class="title">BRIGHT PATH<br>DOJO</h1>
    <p class="tagline">Focus Your Child's Potential</p>
    <p class="url">www.<em>brightpathdojo</em>.example</p>
  </section>
</main>
</body>
</html>
```